【 概要 】 当社は、ペットフード商品を取り扱っております。 引き続き、犬用のおやつジャーキー商品ラベルデザインをお願いいたします。 作成物:犬のおやつで内容は、「鮭を使用した完全無添加、ヒューマングレードのジャーキー」です。 【 依頼詳細 】 ■詳細は、添付のエクセルデータに記載しております。 商品名:「北海道産 カリッと鶏ささみ棒(スライスタイプ)」です。 ■イメージ:エクセルデータにイメージを記載しています。 ※鮭の和と高級なイメージの中で親しみが出るようなソフトな雰囲気を意識していただきたいです。愛犬のおやつなので。 愛犬に安心安全で高級なおやつをあげたいと思いたくなるようなデザインを望んでいます。 ■ターゲット:愛犬に安心安全で高級なおやつをあげたいと思ってくれる飼い主様 【お願い】 採用となった方に修正などのご協力をお願いする場合がありますのでご了承ください。 ※デザインのイメージや柔軟なご対応にご協力いただけた場合、当社でも今後もデザインのご依頼を定期的にさせていただきたいと考えております。 ・編集可能なファイル形式(ai) ・PDFデータ ・フォトショップ(.psd) ・高解像度JPG形式(JPG) 【 契約金額(税込) 】 33,000円(税込) ※契約金額(税込)からシステム利用料を差し引いた金額が、ワーカーさまの受取金額となります ・採用されたデザインの著作権は弊社に譲渡いただき、同意いただいた上でご応募ください。 ■禁止事項 ------------------ ・他で登録されているデザインや転用など、他社の知的財産権を侵すこと ・他のクライアントへ既に提案した内容の転用など -------------------------------- 採用された方は継続的に仕事を依頼する場合もあります。 末永くお付き合いできるデザイナー様を探しております。 素敵なデザインに仕上げるために、ぜひお力をお貸しください その他ご質問等ありましたら、気軽にお問い合わせください。 ご応募をお待ちしております! |
こちらの作品が、当社としてもブランドのイメージに合ったデザインでした。ワーカー様もご対応が丁寧な方で好感をもてました。
皆様、素敵なデザインをご提案いただきありがとうございました。こんなにもご応募いただけたこと、うれしく存じます。また、機会があればご依頼させていただきますのでよろしくお願いいたします。

```html
<!DOCTYPE html>
<html lang="ja">
<head>
<meta charset="utf-8">
<title>カリッと鶏ささみ棒 ラベル</title>
<link href="https://fonts.googleapis.com/css2?family=Yuji+Boku&family=Zen+Old+Mincho:wght@700;900&display=swap" rel="stylesheet">
<style>
  :root{
    --paper:#e1e6ee;
    --ink:#1d1d1f;
    --stamp:#d3202a;
    --salmon:#e9a1a8;
    --salmon-deep:#d98690;
    --mist:#c9ced6;
    --bubble:#ffffff;
    --jerky:#6b4a2e;
    --wood:#c89a62;
    --dog:#d8b48a;
  }
  *{margin:0;padding:0;box-sizing:border-box}
  html,body{width:840px;height:1200px;overflow:hidden;background:var(--paper)}
  .label{position:relative;width:840px;height:1200px;background:var(--paper);overflow:hidden;
    font-family:"Zen Old Mincho",serif;color:var(--ink)}
  .logo-slot{position:absolute;left:21px;top:16px;width:166px;height:91px;border:2px dashed #555;border-radius:16px;
    display:flex;align-items:center;justify-content:center;font-weight:900;font-size:30px;letter-spacing:4px}
  .category{position:absolute;left:232px;top:30px;font-size:30px;font-weight:700;letter-spacing:2px}
  .hero-art{position:absolute;left:80px;top:105px;width:730px;height:740px;border-radius:48% 52% 46% 54%;
    background:radial-gradient(ellipse at 50% 50%, var(--mist) 0%, var(--salmon) 38%, rgba(233,161,168,.55) 60%, rgba(225,230,238,0) 72%)}
  .origin-stamp{position:absolute;left:581px;top:155px;width:160px;height:144px;border:6px solid var(--stamp);border-radius:10px;
    display:grid;grid-template-columns:1fr 1fr;grid-template-rows:1fr 1fr;align-items:center;justify-items:center;
    font-family:"Yuji Boku",serif;color:var(--stamp);font-size:58px;line-height:1;background:rgba(255,255,255,.35)}
  .origin-stamp span:nth-child(1){grid-column:2;grid-row:1}
  .origin-stamp span:nth-child(2){grid-column:1;grid-row:1}
  .origin-stamp span:nth-child(3){grid-column:1;grid-row:2}
  .origin-stamp span:nth-child(4){grid-column:2;grid-row:2}
  .name-lead{position:absolute;left:128px;top:250px;font-family:"Yuji Boku",serif;font-size:78px;letter-spacing:6px;
    transform:rotate(-4deg)}
  .name-main{position:absolute;left:250px;top:360px;font-family:"Yuji Boku",serif;font-size:330px;line-height:1}
  .name-tail{position:absolute;left:505px;top:700px;font-family:"Yuji Boku",serif;font-size:76px;letter-spacing:8px}
  .claim-bubble{position:absolute;left:112px;top:878px;width:262px;height:124px}
  .claim-bubble svg{position:absolute;inset:0}
  .claim-text{position:absolute;inset:0;display:flex;flex-direction:column;align-items:center;justify-content:center;
    gap:14px;font-weight:900;font-size:23px;letter-spacing:2px}
  .dogs-art{position:absolute;left:0;top:1052px;width:410px;height:148px;border-radius:70px 90px 0 0;
    background:linear-gradient(180deg,#e8d6bf 0%,var(--dog) 55%,#b98f67 100%)}
  .jerky-art{position:absolute;left:472px;top:890px;width:340px;height:320px;border-radius:50%;
    background:radial-gradient(circle at 45% 45%, var(--jerky) 0%, #8a5f3a 45%, var(--wood) 72%, #a87b4a 100%)}
</style>
</head>
<body>
<main class="label">
  <div class="logo-slot">ロゴ</div>
  <p class="category">〈犬用おやつ〉</p>

  <div class="hero-art" role="img" aria-label="淡いピンクの筆の渦の中に描かれた鮭のイラスト"></div>

  <div class="origin-stamp" aria-label="北海道産">
    <span>海</span><span>北</span><span>道</span><span>産</span>
  </div>

  <h1 class="product-name">
    <span class="name-lead">カリッと</span>
    <span class="name-main">鶏</span>
    <span class="name-tail">ささみ棒</span>
  </h1>

  <div class="claim-bubble">
    <svg width="262" height="124" viewBox="0 0 262 124" aria-hidden="true">
      <path d="M131 4 C205 4 258 24 258 56 C258 88 205 106 140 106 L120 122 L116 104 C52 100 4 84 4 56 C4 24 57 4 131 4 Z"
            fill="var(--bubble)" stroke="#222" stroke-width="2"/>
    </svg>
    <div class="claim-text"><span>完全無添加</span><span>ヒューマングレード</span></div>
  </div>

  <div class="dogs-art" role="img" aria-label="並んで座る犬たちのイラスト"></div>
  <div class="jerky-art" role="img" aria-label="木皿に盛られたジャーキーの写真"></div>
</main>
</body>
</html>
```